International Digitally Led Media Agency Requires a New Website

Brief Outline

• We are a growing business that has been established for approximately 2 years.

• Our current website did the job when Corvend Media began but it has not developed and progressed alongside the business (currently it does not represent nor portray the business appropriately).

• Corvend Media is a digitally led media agency that has numerous arms; 1) production based work (e.g. Paid Advertising, etc.) 2) consultancy and 3) Offline media (such as outdoor, TV, Radio)

• The business is globally focused and the website must reflect this.

• The new website is to portray the business more professionally with thought leadership at the forefront.

• The tone and voice of the website is to be clear, concise and straight talking.

• The website isn't to be a driver of new business (e.g. conversion based for enquiries) but is to support external new business activities. However, the website is to support the thought leadership marketing (specifically around content marketing - webinars, whitepapers, social, etc).

• We must be able to edit/upload/add content to the website very easily.

The current website is www.corvend-media.example

Current clients include
J&T - www.j&t.example
Folmary Trudesse - www.ft.example
KX Glow - www.kxglow.example
Lungwise UK - www.lungwise.example.uk
The Vantry Academy - www.vantry-academy.example.uk
Hale Retirement - www.haleretirement.example
Quillet Credit - www.quilletcredit.example.uk
DLMorvat - www.dl-morvat.example.uk
Perravine Lodging Collective - www.plc-lodging.example
Brindlewick - www.brindlewick.example
Varnique - www.varniqueit.example

Reason: We gave some delayed feedback to some desginers looking to enter the project and want to give them a chance to submit their designs.

Target Market(s)

Key decision makers within brands. Marketing Executives/Managers/Directors, Procurement Executives/Managers/Directors, Company Owners, CEO's /MD's

Industry/Entity Type

Business

Coding

Coded - Design and coding required

Number of Pages Required

5+ page

Font styles to use
Sans Serif

Requirements
Must have
• We definitely want video capability and the ability to add pages ourselves.
• We would like the layout to look something like
• HOME
•   
• 7dash3 > CASE STUDIES
• WHAT WE DO > CASE STUDIES
•  
• CONTACT
•  
• CLIENT LOGIN
Nice to have
• Social feeds

```html
<!DOCTYPE html>
<html lang="en">
<head>
<meta charset="utf-8">
<title>Corvend Media</title>
<link href="https://fonts.googleapis.com/css2?family=Roboto+Condensed:wght@400;700&family=Open+Sans:wght@400;600;700&display=swap" rel="stylesheet">
<style>
:root{
  --crimson:#9b1b35;
  --crimson-dark:#821528;
  --ink:#2b2b2b;
  --text:#6d6d6d;
  --grey-bg:#ececec;
  --white:#ffffff;
  --charcoal:#333333;
  --field:#ffffff;
  --field-line:#d6d6d6;
}
*{margin:0;padding:0;box-sizing:border-box}
html,body{width:1200px;height:3593px;overflow:hidden}
body{font-family:"Open Sans",sans-serif;color:var(--text);background:var(--white);position:relative}
.cond{font-family:"Roboto Condensed",sans-serif}
section,header,nav,footer{position:absolute;left:0;width:1200px}
.abs{position:absolute}
.accent{color:var(--crimson)}

/* header */
.site-header{top:0;height:113px;background:var(--white)}
.brand{left:75px;top:12px;display:flex;align-items:center;gap:14px}
.brand-mark{width:84px;height:84px;border-radius:50%;border:3px solid var(--crimson)}
.brand-name{font-family:"Roboto Condensed",sans-serif;font-size:26px;letter-spacing:3px;color:var(--charcoal);font-weight:400}
.call-label{left:566px;top:46px;font-family:"Roboto Condensed",sans-serif;font-size:21px;color:var(--charcoal)}
.call-icon{left:680px;top:30px;width:56px;height:56px;border-radius:50%;border:3px solid var(--crimson)}
.call-number{left:750px;top:45px;font-family:"Roboto Condensed",sans-serif;font-size:22px;color:var(--charcoal)}
.login-btn{left:915px;top:34px;width:206px;height:50px;background:var(--crimson);color:var(--white);font-family:"Roboto Condensed",sans-serif;font-size:20px;display:flex;align-items:center;padding-left:22px}
.login-btn .arrow{position:absolute;right:0;top:0;width:50px;height:50px;background:var(--charcoal);display:flex;align-items:center;justify-content:center}

/* nav */
.main-nav{top:113px;height:69px;background:var(--crimson)}
.main-nav a{position:absolute;top:0;height:69px;line-height:69px;color:var(--white);font-family:"Roboto Condensed",sans-serif;font-size:17px;text-decoration:none;transform:translateX(-50%)}
.main-nav a.current{background:var(--charcoal);width:125px;text-align:center}

/* hero */
.hero{top:182px;height:484px;background:linear-gradient(180deg,#3a2a2a 0%,#8a5a3a 35%,#d98a3a 52%,#5a3a30 70%,#2a2526 100%)}
.hero h1{position:absolute;left:0;width:1200px;top:170px;text-align:center;color:var(--white);font-family:"Open Sans",sans-serif;font-weight:400;font-size:52px;line-height:66px;text-shadow:0 2px 6px rgba(0,0,0,.5)}
.hero h1 .big{font-size:66px;font-weight:700}
.hero h1 b{font-weight:700}

/* services */
.services{top:666px;height:261px;background:var(--crimson)}
.service{position:absolute;top:0;width:330px;text-align:center;color:var(--white);transform:translateX(-50%)}
.service .badge{position:absolute;left:103px;top:-57px;width:124px;height:124px;border-radius:50%;background:var(--white);display:flex;align-items:center;justify-content:center}
.service h3{position:absolute;top:95px;width:330px;font-family:"Roboto Condensed",sans-serif;font-size:19px;font-weight:700}
.service p{position:absolute;top:125px;width:330px;font-size:14px;line-height:22px}
.service .chev{position:absolute;top:202px;left:156px}

/* welcome */
.welcome{top:927px;height:398px;background:var(--white);text-align:center}
.section-title{position:absolute;left:0;width:1200px;text-align:center;font-family:"Roboto Condensed",sans-serif;font-size:42px;font-weight:400;color:var(--charcoal)}
.welcome p{position:absolute;left:168px;width:864px;font-size:14px;line-height:30px}
.btn{position:absolute;height:55px;background:var(--crimson);color:var(--white);font-family:"Roboto Condensed",sans-serif;font-size:19px;display:flex;align-items:center;justify-content:center}

/* who */
.who{top:1325px;height:466px;background:var(--grey-bg)}
.video-frame{left:100px;top:59px;width:427px;height:345px}
.who h2{position:absolute;left:563px;top:55px;font-family:"Roboto Condensed",sans-serif;font-size:42px;font-weight:400;color:var(--charcoal)}
.who .lead{position:absolute;left:568px;top:112px;font-size:16px;font-weight:600;color:var(--charcoal)}
.who p.body{position:absolute;left:568px;width:560px;font-size:14px;line-height:25px}

/* work */
.work{top:1791px;height:460px;background:var(--crimson);color:var(--white)}
.work .section-title{color:var(--white)}
.work .sub{position:absolute;left:0;width:1200px;top:112px;text-align:center;font-size:14px;color:#d8a0ab}
.case-img{position:absolute;top:161px;width:206px;height:148px}
.case{position:absolute;top:166px;width:300px}
.case h4{font-family:"Roboto Condensed",sans-serif;font-size:17px;font-weight:700;line-height:22px;text-transform:uppercase}
.case p{margin-top:10px;font-size:14px;line-height:20px}
.case .more{margin-top:6px;font-size:14px;font-weight:600}
.btn-outline{position:absolute;left:515px;top:341px;width:168px;height:55px;border:2px solid var(--white);color:var(--white);font-family:"Roboto Condensed",sans-serif;font-size:19px;display:flex;align-items:center;justify-content:center}

/* blog */
.blog{top:2251px;height:475px;background:var(--white)}
.post{position:absolute;top:132px;width:249px}
.post .thumb{width:249px;height:156px}
.post .date{margin-top:18px;font-size:13px;font-style:italic;color:var(--crimson);display:flex;align-items:center;gap:7px}
.post h4{margin-top:10px;font-family:"Roboto Condensed",sans-serif;font-size:18px;font-weight:400;color:var(--charcoal)}
.post p{margin-top:6px;font-size:13px;line-height:19px}

/* contact */
.contact{top:2726px;height:479px;background:var(--grey-bg)}
.contact .intro{position:absolute;left:168px;width:864px;top:122px;text-align:center;font-size:14px;line-height:28px}
.field{position:absolute;background:var(--field);border:1px solid var(--field-line);font-size:14px;color:#999;padding:16px 14px}

/* clients */
.clients{top:3205px;height:158px;background:var(--white)}
.slide-arrow{position:absolute;top:57px;width:44px;height:44px;border-radius:50%;border:2px solid #bbb;display:flex;align-items:center;justify-content:center}
.client{position:absolute;top:52px;height:54px;display:flex;align-items:center;gap:8px;font-family:"Open Sans",sans-serif;font-weight:700;font-size:16px;transform:translateX(-50%);white-space:nowrap}
.client .dot{width:36px;height:36px;flex:none}

/* footer */
.site-footer{top:3363px;height:230px;background:var(--crimson);color:var(--white)}
.foot-nav a{position:absolute;top:24px;height:38px;line-height:38px;color:var(--white);text-decoration:none;font-size:15px;transform:translateX(-50%)}
.foot-nav a.current{border:2px solid var(--white);border-radius:20px;width:86px;text-align:center;line-height:34px}
.social{position:absolute;top:21px;width:46px;height:46px;border-radius:50%;background:var(--charcoal)}
.footer-title{position:absolute;left:79px;top:106px;font-family:"Roboto Condensed",sans-serif;font-weight:700;font-size:18px}
.foot-item{position:absolute;top:138px;display:flex;align-items:center;gap:14px;font-size:13px;line-height:19px}
.foot-icon{width:50px;height:50px;border-radius:50%;border:2px solid var(--white);display:flex;align-items:center;justify-content:center;flex:none}
.foot-icon.solid{background:#222;border-color:#222}
.copy{position:absolute;left:881px;top:153px;font-size:13px;line-height:19px;color:#e9c5cc}
.copy b{color:var(--white)}
</style>
</head>
<body>

<header class="site-header">
  <div class="brand abs"><span class="brand-mark"></span><span class="brand-name">CORVEND MEDIA</span></div>
  <div class="call-label abs">CALL US ON</div>
  <div class="call-icon abs">
    <svg width="50" height="50" viewBox="0 0 50 50"><path d="M17 15c2-2 4 0 5 2l1 3c0 2-2 2-2 3 1 3 4 6 7 7 1 0 1-2 3-2l3 1c2 1 4 3 2 5-3 3-6 3-10 1-5-3-9-7-11-12-1-3 0-6 2-8z" fill="#9b1b35"/><path d="M28 14a8 8 0 0 1 8 8M28 9a13 13 0 0 1 13 13" stroke="#9b1b35" stroke-width="2.5" fill="none"/></svg>
  </div>
  <div class="call-number abs">+44 20 7946 0321</div>
  <div class="login-btn abs">CLIENT LOGIN<span class="arrow"><svg width="18" height="22" viewBox="0 0 18 22"><path d="M4 2l10 9-10 9" stroke="#fff" stroke-width="4" fill="none"/></svg></span></div>
</header>

<nav class="main-nav">
  <a class="current" href="#" style="left:141px">HOME</a>
  <a href="#" style="left:290px">OUR WORK</a>
  <a href="#" style="left:435px">WHO WE ARE</a>
  <a href="#" style="left:595px">CLIENT LOGIN</a>
  <a href="#" style="left:728px">BLOG</a>
  <a href="#" style="left:845px">CONTACT</a>
  <svg class="abs" style="left:1095px;top:22px" width="26" height="26" viewBox="0 0 26 26"><circle cx="11" cy="11" r="7.5" stroke="#3a0d17" stroke-width="3" fill="none"/><path d="M16.5 16.5l6 6" stroke="#3a0d17" stroke-width="3.5"/></svg>
</nav>

<section class="hero" role="img" aria-label="Photo of a city skyline at sunset above a busy rail yard">
  <h1><span class="big">G</span>ot the feeling your digital marketing<br>just isn't quite '<b>there</b>'?</h1>
</section>

<section class="services">
  <div class="service" style="left:237px">
    <div class="badge"><svg width="70" height="60" viewBox="0 0 70 60"><circle cx="20" cy="14" r="10" fill="#9b1b35"/><circle cx="42" cy="14" r="10" fill="#9b1b35"/><rect x="8" y="26" width="40" height="26" rx="4" fill="#9b1b35"/><path d="M50 34l14-8v26l-14-8z" fill="#9b1b35"/></svg></div>
    <h3>PRODUCTION BASED WORK</h3>
    <p>We make your brand famous. To do this we opt-<br>imise your website or any digital assets you have,<br>so they can be found online.</p>
    <svg class="chev" width="18" height="18" viewBox="0 0 18 18"><path d="M3 2l6 6 6-6M3 9l6 6 6-6" stroke="#fff" stroke-width="2" fill="none"/></svg>
  </div>
  <div class="service" style="left:599px">
    <div class="badge"><svg width="66" height="64" viewBox="0 0 66 64"><rect x="14" y="4" width="38" height="20" rx="3" fill="#9b1b35"/><circle cx="16" cy="36" r="6" fill="#9b1b35"/><circle cx="33" cy="34" r="6" fill="#9b1b35"/><circle cx="50" cy="36" r="6" fill="#9b1b35"/><rect x="8" y="44" width="16" height="16" rx="4" fill="#9b1b35"/><rect x="25" y="42" width="16" height="18" rx="4" fill="#9b1b35"/><rect x="42" y="44" width="16" height="16" rx="4" fill="#9b1b35"/></svg></div>
    <h3>CONSULTANCY</h3>
    <p>We make your brand famous. To do this we opt -<br>imise your website or any digital assets you have,<br>so they can be found online.</p>
    <svg class="chev" width="18" height="18" viewBox="0 0 18 18"><path d="M3 2l6 6 6-6M3 9l6 6 6-6" stroke="#fff" stroke-width="2" fill="none"/></svg>
  </div>
  <div class="service" style="left:956px">
    <div class="badge"><svg width="70" height="60" viewBox="0 0 70 60"><path d="M8 22h12l26-16v48L20 38H8z" fill="#9b1b35"/><rect x="16" y="38" width="9" height="16" fill="#9b1b35"/><path d="M52 22c4 4 4 12 0 16M57 16c8 8 8 20 0 28" stroke="#9b1b35" stroke-width="3" fill="none"/></svg></div>
    <h3>OFFLINE MEDIA</h3>
    <p>We make your brand famous. To do this we opt -<br>imise your website or any digital assets you have,<br>so they can be found online.</p>
    <svg class="chev" width="18" height="18" viewBox="0 0 18 18"><path d="M3 2l6 6 6-6M3 9l6 6 6-6" stroke="#fff" stroke-width="2" fill="none"/></svg>
  </div>
</section>

<section class="welcome">
  <h2 class="section-title" style="top:54px">Welcome To <span class="accent">Corvend Media</span></h2>
  <p style="top:128px">There are too many large agency networks. Consolidation is everywhere, giving clients less choice and choking media creativity for the benefit of perceived economies of scale. There are too few agencies being transparent. Do you really know how your agency makes its revenue? Are their decisions based on what is best for your brand or are there other incentives involved?</p>
  <p style="top:218px">There are too many large agency networks. Consolidation is everywhere, giving clients less choice and choking media creativity for the benefit of perceived economies of scale. There are too few agencies being transparent.</p>
  <div class="btn" style="left:517px;top:275px;width:166px">KNOW MORE</div>
</section>

<section class="who">
  <div class="video-frame abs" role="img" aria-label="Desktop monitor playing the agency video 'Corvend Media - Who We Are'" style="background:linear-gradient(180deg,#2a2a2a 0 9%,#f4f2ee 9% 78%,#c9c9c9 78% 84%,#e2e2e2 84% 100%);border-radius:8px"></div>
  <h2>Who <span class="accent">We Are?</span></h2>
  <div class="lead">We are Corvend Media We believe..</div>
  <p class="body" style="top:145px">There are too many large agency networks. Consolidation is everywhere, giving clients less choice and choking media creativity for the benefit of perceived economies of scale.</p>
  <p class="body" style="top:232px">There are too few agencies being transparent. Do you really know how your agency makes its revenue? Are their decisions based on what is best for your brand or are there other incentives involved? Too many of these agencies put quality of work second to income.</p>
  <div class="btn" style="left:568px;top:344px;width:165px">KNOW MORE</div>
</section>

<section class="work">
  <h2 class="section-title" style="top:58px"><span style="color:var(--charcoal)">Our</span> Work</h2>
  <div class="sub">Case Study</div>
  <div class="case-img" role="img" aria-label="Close-up photo of a camera lens" style="left:77px;background:radial-gradient(circle at 60% 50%,#6a5a50 0,#2a2220 45%,#c8bfb5 80%)"></div>
  <div class="case" style="left:302px">
    <h4>Mira's world is unraveling. Her lover leaves her</h4>
    <p>And then she meets his wife. And his son. Our challenge was to launch a new musical in London's West End.</p>
    <div class="more">Read More... »</div>
  </div>
  <div class="case-img" role="img" aria-label="Photo of a woman working at a desk by a window" style="left:604px;background:linear-gradient(135deg,#d8d2c6,#8a7e70 60%,#5a4e44)"></div>
  <div class="case" style="left:826px">
    <h4>Heart not hype. Surpass expectations</h4>
    <p>Threlk exists to multiply human performance. Corvend exists to deliver amazing work for amazing brands. Our role was to.</p>
    <div class="more">Read More...</div>
  </div>
  <div class="btn-outline">VIEW ALL</div>
</section>

<section class="blog">
  <h2 class="section-title" style="top:58px">Latest <span class="accent">Blog</span></h2>
  <div class="post" style="left:79px">
    <div class="thumb" role="img" aria-label="Photo of a hand using a smartphone" style="background:linear-gradient(135deg,#6a7a8a,#2a3440 60%,#c8ccd0)"></div>
    <div class="date"><svg width="13" height="13" viewBox="0 0 13 13"><rect x="1" y="2" width="11" height="10" fill="none" stroke="#9b1b35" stroke-width="1.5"/><path d="M1 5h11" stroke="#9b1b35" stroke-width="1.5"/></svg>Feb 24, 2016</div>
    <h4>Fewer ads on Searchly</h4>
    <p>Searchly has just implemented a change that will reduce the ad-depth.</p>
  </div>
  <div class="post" style="left:342px">
    <div class="thumb" role="img" aria-label="Photo of a keyboard and coffee cup on a desk" style="background:linear-gradient(180deg,#e8e4de,#c8b8a2 60%,#9a8670)"></div>
    <div class="date"><svg width="13" height="13" viewBox="0 0 13 13"><rect x="1" y="2" width="11" height="10" fill="none" stroke="#9b1b35" stroke-width="1.5"/><path d="M1 5h11" stroke="#9b1b35" stroke-width="1.5"/></svg>Feb 24, 2016</div>
    <h4>Copy writing and paid search</h4>
    <p>Lorem Ipsum is simply dummy text of the printing and typesetting..</p>
  </div>
  <div class="post" style="left:608px">
    <div class="thumb" role="img" aria-label="Photo of a business meeting" style="background:linear-gradient(135deg,#3a3a40,#7a6e66 55%,#c8c0b8)"></div>
    <div class="date"><svg width="13" height="13" viewBox="0 0 13 13"><rect x="1" y="2" width="11" height="10" fill="none" stroke="#9b1b35" stroke-width="1.5"/><path d="M1 5h11" stroke="#9b1b35" stroke-width="1.5"/></svg>Feb 25, 2016</div>
    <h4>Linkfold and B2B marketing</h4>
    <p>why they are far behind the other paid social when they should own it?</p>
  </div>
  <div class="post" style="left:872px">
    <div class="thumb" role="img" aria-label="Photo of a glowing lightbulb at sunset" style="background:linear-gradient(180deg,#f6d27a,#f0a030 55%,#5a3a20)"></div>
    <div class="date"><svg width="13" height="13" viewBox="0 0 13 13"><rect x="1" y="2" width="11" height="10" fill="none" stroke="#9b1b35" stroke-width="1.5"/><path d="M1 5h11" stroke="#9b1b35" stroke-width="1.5"/></svg>Dec 03, 2015</div>
    <h4>The price of paid search</h4>
    <p>Paid search is getting more expensive every year. It doesn't really.</p>
  </div>
</section>

<section class="contact">
  <h2 class="section-title" style="top:58px">Contact <span class="accent">Us</span></h2>
  <p class="intro">If you would like to chat then please get in touch. Corvend Media are based in London's West End on Larkmoor Place. The closest tube stations are Halden Court Road and Merrow Circus.</p>
  <div class="field" style="left:168px;top:184px;width:282px;height:52px">Name*</div>
  <div class="field" style="left:460px;top:184px;width:282px;height:52px">Email*</div>
  <div class="field" style="left:752px;top:184px;width:280px;height:52px">Phone*</div>
  <div class="field" style="left:168px;top:249px;width:864px;height:100px">Message*</div>
  <div class="btn" style="left:522px;top:359px;width:156px">SUBMIT</div>
</section>

<section class="clients">
  <div class="slide-arrow" style="left:76px"><svg width="12" height="16" viewBox="0 0 12 16"><path d="M9 2L3 8l6 6" stroke="#999" stroke-width="2" fill="none"/></svg></div>
  <div class="client" style="left:235px;color:#6a2a8a"><span class="dot" style="background:#6a2a8a"></span>Lungwise UK</div>
  <div class="client" style="left:420px;color:#222">Hale Retirement</div>
  <div class="client" style="left:600px;color:#e0701a">Perravine Lodging</div>
  <div class="client" style="left:778px;color:#1a3a8a">Brindlewick</div>
  <div class="client" style="left:977px;color:#d0258a"><span class="dot" style="background:#d0258a;border-radius:50%"></span>Folmary Trudesse</div>
  <div class="slide-arrow" style="left:1080px"><svg width="12" height="16" viewBox="0 0 12 16"><path d="M3 2l6 6-6 6" stroke="#999" stroke-width="2" fill="none"/></svg></div>
</section>

<footer class="site-footer">
  <div class="foot-nav">
    <a class="current" href="#" style="left:121px">Home</a>
    <a href="#" style="left:227px">Our Work</a>
    <a href="#" style="left:350px">Who We Are</a>
    <a href="#" style="left:479px">Client Login</a>
    <a href="#" style="left:568px">Blog</a>
    <a href="#" style="left:649px">Contact</a>
  </div>
  <span class="social" style="left:952px" aria-label="Video channel"></span>
  <span class="social" style="left:1014px" aria-label="Video channel"></span>
  <span class="social" style="left:1074px" aria-label="Social feed"></span>
  <div class="footer-title">CONTACT US</div>
  <div class="foot-item" style="left:79px">
    <span class="foot-icon solid"><svg width="20" height="26" viewBox="0 0 20 26"><path d="M10 1a8 8 0 0 1 8 8c0 6-8 16-8 16S2 15 2 9a8 8 0 0 1 8-8z" fill="#fff"/><circle cx="10" cy="9" r="3" fill="#222"/></svg></span>
    <span>20 Larkmoor Place London,<br>W1X 9ZZ</span>
  </div>
  <div class="foot-item" style="left:346px">
    <span class="foot-icon"><svg width="24" height="24" viewBox="0 0 24 24"><path d="M6 3c1-1 3 0 4 2l1 2c0 2-2 2-1 3 1 2 3 4 5 5 1 0 1-2 3-1l2 1c2 1 2 3 1 4-2 2-5 2-8 0-4-2-7-5-9-9-1-3 0-5 2-7z" fill="#fff"/></svg></span>
    <span>+44 20 7946 0321</span>
  </div>
  <div class="foot-item" style="left:595px">
    <span class="foot-icon"><svg width="24" height="18" viewBox="0 0 24 18"><rect x="1" y="1" width="22" height="16" fill="none" stroke="#fff" stroke-width="2"/><path d="M1 1l11 9 11-9" stroke="#fff" stroke-width="2" fill="none"/></svg></span>
    <span>contact@corvend-media.example</span>
  </div>
  <div class="copy">© <b>Corvend Media</b> - 2016 All rights<br>reserved.</div>
</footer>

</body>
</html>
```